Corporate Design für Rechtsanwalt (Arbeitsrecht und Gesellschaftsrecht)
Zielgruppe
Rechtsanwalt (Arbeitsrecht und Gesellschaftsrecht)
Aufgabenstellung
Benötigt wird ein schlichtes und modernes Corporate Design für einen Anwalt, der sich vorwiegend mit Arbeitsrecht (Arbeitnehmer wie Arbeitgeber) und Gesellschaftsrecht befasst. Das Logo soll Professionalität und Seriosität vermitteln. Ein Paragraphenzeichen oder eine Waage sollen bitte nicht enthalten sein, da dies „alle“ Rechtsanwälte haben. Die Rechtsgebiete Arbeitsrecht und Gesellschaftsrecht sollen nicht im Logo enthalten sein.
Folgender Inhalt muss untergebracht werden:
Tobias Renz
Rechtsanwalt
Auf dem Briefkopf müssen Bankverbindung, St.-Nr., USt-ID, Internetadresse und Kontaktdaten (Adresse, Telefon, Fax und Mailadresse) untergebracht werden. Diese Daten müssen selbstständig abänderbar sein.
Notwendig sind: Logo, Briefkopf und Visitenkarte.

```html
<!DOCTYPE html>
<html lang="de">
<head>
<meta charset="utf-8">
<title>Tobias Renz – Rechtsanwalt – Geschäftsausstattung</title>
<link href="https://fonts.googleapis.com/css2?family=Open+Sans:wght@400;600;700&display=swap" rel="stylesheet">
<style>
  :root{
    --navy:#1f3c63;
    --grey:#a4a7b2;
    --paper:#f7f7f7;
    --white:#ffffff;
    --ink:#2a2a2a;
    --muted:#777a80;
    --bg:#ececec;
  }
  *{box-sizing:border-box;margin:0;padding:0}
  html,body{width:698px;height:1200px;overflow:hidden;background:var(--bg);font-family:"Open Sans",Arial,sans-serif;color:var(--ink)}
  .sheet{position:relative;width:698px;height:1200px}

  /* brand name lockup */
  .brand{display:flex;flex-direction:column;align-items:center;text-align:center}
  .brand__name{font-weight:400;text-transform:uppercase;letter-spacing:.06em;white-space:nowrap}
  .brand__role{display:flex;align-items:center;gap:3px;font-weight:400;letter-spacing:.22em;text-transform:uppercase;color:var(--grey);white-space:nowrap}
  .brand__role::before,.brand__role::after{content:"";display:block;width:12px;height:.5px;background:var(--grey)}

  /* business cards */
  .card{position:absolute;width:159px;height:91px;overflow:hidden;box-shadow:0 1px 3px rgba(0,0,0,.25)}
  .card--front{background:var(--navy);display:flex;align-items:center;justify-content:center}
  .card--front .brand__name{color:var(--white);font-size:10.5px}
  .card--front .brand__role{font-size:4.2px;margin-top:1px;color:#c3c6cf}
  .card--front .brand__role::before,.card--front .brand__role::after{background:#c3c6cf}
  .card--back{background:var(--paper)}
  .card--back .studio{position:absolute;left:10px;top:24px;font-size:4.4px}
  .card--back .brand{position:absolute;right:12px;top:34px}
  .card--back .brand__name{color:var(--navy);font-size:9.5px}
  .card--back .brand__role{font-size:3.8px}
  .card__address,.card__contact{position:absolute;top:61px;font-size:3.3px;line-height:4.2px}
  .card__address{left:11px}
  .card__contact{left:99px}
  .card__band{position:absolute;left:0;bottom:0;width:159px;height:9px}

  /* letterheads */
  .letter{position:absolute;top:392px;width:247px;height:352px;background:var(--paper);box-shadow:0 1px 3px rgba(0,0,0,.2);overflow:hidden}
  .letter .brand{position:absolute;top:37px}
  .letter .brand__name{color:var(--navy);font-size:8px}
  .letter .brand__role{font-size:3.2px;letter-spacing:.2em}
  .letter .brand__role::before,.letter .brand__role::after{width:9px}
  .letter--left .brand{left:19px}
  .letter--right .brand{right:12px}
  .letter__sender{position:absolute;left:19px;top:53px;font-size:2.8px;padding-bottom:1px;border-bottom:.5px solid var(--ink)}
  .letter__recipient{position:absolute;left:28px;top:75px;font-size:3.5px;line-height:5.3px;color:var(--muted)}
  .letter__recipient strong{display:block;font-size:5.4px;color:var(--ink);font-weight:600;margin-bottom:1px}
  .letter__date{position:absolute;right:28px;top:100px;font-size:3.5px;color:var(--muted)}
  .letter__body{position:absolute;left:28px;top:116px;width:191px;font-size:3.5px;line-height:5.35px;color:var(--muted);text-align:justify}
  .letter__body p{margin-bottom:5.3px}
  .letter__signature{position:absolute;left:28px;top:253px;width:46px;height:8px;background:linear-gradient(90deg,#d8d8d8,#e8e8e8)}
  .letter__signer{position:absolute;left:28px;top:265px;font-size:4.8px;font-weight:600;line-height:6px}
  .letter__signer span{display:block;font-size:3.5px;font-weight:400;color:var(--muted)}
  .fold{position:absolute;left:0;width:7px;height:.5px;background:var(--ink)}
  .letter__footer{position:absolute;left:20px;right:20px;top:330px;border-top:.6px solid var(--ink);padding-top:5px;display:flex;justify-content:space-between;font-size:2.4px;line-height:3.1px}
  .letter__footer div{padding-right:8px;border-right:.5px solid var(--ink)}
  .letter__footer div:last-child{border-right:0;padding-right:0}

  /* envelopes */
  .envelope{position:absolute;left:201px;width:296px;height:153px;background:linear-gradient(135deg,#fafafa,#eeeeee);box-shadow:0 1px 3px rgba(0,0,0,.2);overflow:hidden}
  .envelope--front{top:769px}
  .envelope--front .brand{position:absolute;left:21px;top:38px}
  .envelope__window{position:absolute;left:21px;top:83px;width:117px;height:54px;border-radius:3px;background:#e4e4e4}
  .envelope--back{top:943px}
  .envelope__flap{position:absolute;left:0;top:0}
  .envelope--back .brand{position:absolute;right:12px;bottom:9px}
  .envelope .brand__name{color:var(--navy);font-size:8px}
  .envelope .brand__role{font-size:3.2px}
  .envelope .brand__role::before,.envelope .brand__role::after{width:9px}
</style>
</head>
<body>
<main class="sheet">

  <!-- Business cards: row 1 -->
  <section class="card card--front" style="left:97px;top:67px">
    <div class="brand"><div class="brand__name">Tobias Renz</div><div class="brand__role">Rechtsanwalt</div></div>
  </section>
  <section class="card card--back" style="left:269px;top:67px">
    <div class="studio">Entwurfwerk</div>
    <div class="brand"><div class="brand__name">Tobias Renz</div><div class="brand__role">Rechtsanwalt</div></div>
    <div class="card__address">ENTWURFWERK<br>Birkenweg 7<br>D-90402 Nürnberg</div>
    <div class="card__contact">Tel: 089 / 00 00 00 - 00<br>Fax: 089 / 00 00 00 - 0000<br>Mobil: 0178 / 000 00 00<br>info@entwurfwerk.example</div>
    <svg class="card__band" viewBox="0 0 159 9"><rect x="0" y="5.5" width="90" height="3.5" fill="#a4a7b2"/><polygon points="80,9 95,0 159,0 159,9" fill="#1f3c63"/></svg>
  </section>
  <section class="card card--front" style="left:441px;top:67px">
    <div class="brand"><div class="brand__name">Tobias Renz</div><div class="brand__role">Rechtsanwalt</div></div>
  </section>

  <!-- row 2 -->
  <section class="card card--back" style="left:97px;top:171px">
    <div class="studio">Entwurfwerk</div>
    <div class="brand"><div class="brand__name">Tobias Renz</div><div class="brand__role">Rechtsanwalt</div></div>
    <div class="card__address">ENTWURFWERK<br>Birkenweg 7<br>D-90402 Nürnberg</div>
    <div class="card__contact">Tel: 089 / 00 00 00 - 00<br>Fax: 089 / 00 00 00 - 0000<br>Mobil: 0178 / 000 00 00<br>info@entwurfwerk.example</div>
    <svg class="card__band" viewBox="0 0 159 9"><rect x="0" y="5.5" width="90" height="3.5" fill="#a4a7b2"/><polygon points="80,9 95,0 159,0 159,9" fill="#1f3c63"/></svg>
  </section>
  <section class="card card--front" style="left:269px;top:171px">
    <div class="brand"><div class="brand__name">Tobias Renz</div><div class="brand__role">Rechtsanwalt</div></div>
  </section>
  <section class="card card--back" style="left:441px;top:171px">
    <div class="studio">Entwurfwerk</div>
    <div class="brand"><div class="brand__name">Tobias Renz</div><div class="brand__role">Rechtsanwalt</div></div>
    <div class="card__address">ENTWURFWERK<br>Birkenweg 7<br>D-90402 Nürnberg</div>
    <div class="card__contact">Tel: 089 / 00 00 00 - 00<br>Fax: 089 / 00 00 00 - 0000<br>Mobil: 0178 / 000 00 00<br>info@entwurfwerk.example</div>
    <svg class="card__band" viewBox="0 0 159 9"><rect x="0" y="5.5" width="90" height="3.5" fill="#a4a7b2"/><polygon points="80,9 95,0 159,0 159,9" fill="#1f3c63"/></svg>
  </section>

  <!-- row 3 -->
  <section class="card card--front" style="left:97px;top:275px">
    <div class="brand"><div class="brand__name">Tobias Renz</div><div class="brand__role">Rechtsanwalt</div></div>
  </section>
  <section class="card card--back" style="left:269px;top:275px">
    <div class="studio">Entwurfwerk</div>
    <div class="brand"><div class="brand__name">Tobias Renz</div><div class="brand__role">Rechtsanwalt</div></div>
    <div class="card__address">ENTWURFWERK<br>Birkenweg 7<br>D-90402 Nürnberg</div>
    <div class="card__contact">Tel: 089 / 00 00 00 - 00<br>Fax: 089 / 00 00 00 - 0000<br>Mobil: 0178 / 000 00 00<br>info@entwurfwerk.example</div>
    <svg class="card__band" viewBox="0 0 159 9"><rect x="0" y="5.5" width="90" height="3.5" fill="#a4a7b2"/><polygon points="80,9 95,0 159,0 159,9" fill="#1f3c63"/></svg>
  </section>
  <section class="card card--front" style="left:441px;top:275px">
    <div class="brand"><div class="brand__name">Tobias Renz</div><div class="brand__role">Rechtsanwalt</div></div>
  </section>

  <!-- Letterhead: first page -->
  <article class="letter letter--left" style="left:99px">
    <div class="brand"><div class="brand__name">Tobias Renz</div><div class="brand__role">Rechtsanwalt</div></div>
    <div class="letter__sender">ENTWURFWERK &nbsp;|&nbsp; Birkenweg 7 &nbsp;|&nbsp; D-90402 Nürnberg</div>
    <div class="letter__recipient"><strong>Name Surname</strong>Senior Executive<br>Address goes here. Street, City, Country<br>contact@yourmail.com<br>000-987-654-321</div>
    <div class="letter__date">Date, 10 September, 2030</div>
    <span class="fold" style="top:124px"></span>
    <span class="fold" style="top:176px"></span>
    <span class="fold" style="top:250px"></span>
    <div class="letter__body">
      <p>Lorem ipsum dolor sit amet, consectetur adipisicing elit, sed do eiusmod tempor incididunt ut labore et dolore magna aliqua. Ut enim ad minim veniam, quis nostrud exercitation ullamco laboris nisi ut aliquip ex ea commodo consequat. Duis aute irure dolor in reprehenderit in voluptate velit esse cillum dolore eu fugiat nulla pariatur. Excepteur sint occaecat cupidatat non proident, sunt in culpa qui officia deserunt mollit anim id est laborum. Sed ut perspiciatis unde omnis iste natus error sit voluptatem accusantium doloremque laudantium, totam rem aperiam, eaque ipsa quae ab illo inventore veritatis et quasi architecto beatae vitae dicta sunt explicabo. Nemo enim ipsam voluptatem quia voluptas sit aspernatur aut odit aut fugit, sed quia consequuntur magni dolores eos qui ratione voluptatem sequi nesciunt.</p>
      <p>Lorem ipsum dolor sit amet, consectetur adipisicing elit, sed do eiusmod tempor incididunt ut labore et dolore magna aliqua. Ut enim ad minim veniam, quis nostrud exercitation ullamco laboris nisi ut aliquip ex ea commodo consequat. Duis aute irure dolor in reprehenderit in voluptate velit esse cillum dolore eu fugiat nulla pariatur. Excepteur sint occaecat cupidatat non proident, sunt in culpa qui officia deserunt mollit anim id est laborum. Sed ut perspiciatis unde omnis iste natus error sit voluptatem accusantium doloremque laudantium, totam rem aperiam, eaque ipsa quae ab illo inventore veritatis.</p>
      <p>Lorem ipsum dolor sit amet, consectetur adipisicing elit, sed do eiusmod tempor incididunt ut labore et dolore magna aliqua. Ut enim ad minim veniam, quis nostrud exercitation ullamco laboris nisi ut aliquip ex ea commodo consequat.</p>
    </div>
    <div class="letter__signature" role="img" aria-label="Handschriftliche Unterschrift"></div>
    <div class="letter__signer">NAME SURNAME<span>General Manager</span></div>
    <footer class="letter__footer">
      <div>Geschäftsführung: Tobias Renz<br>entwurfwerk.example<br>Sitz: Nürnberg</div>
      <div>Amtsgericht Nürnberg HRB-Nr. 0000<br>EORI-Nr. DE 000 0000<br>USt-IdNr.: DE000 000 000<br>Steuer-Nr.: 000/000/00000</div>
      <div>Stadtbank Süd<br>IBAN DE00 0000 0000 0000 00<br>BIC STBSDEMMXXX</div>
      <div>Kreiskasse Nord<br>IBAN DE00 0000 0000 0000 00<br>BIC KKNODEM1XXX</div>
    </footer>
  </article>

  <!-- Letterhead: following page -->
  <article class="letter letter--right" style="left:354px">
    <div class="brand"><div class="brand__name">Tobias Renz</div><div class="brand__role">Rechtsanwalt</div></div>
    <div class="letter__recipient"><strong>Name Surname</strong>Senior Executive<br>Address goes here. Street, City, Country<br>contact@yourmail.com<br>000-987-654-321</div>
    <div class="letter__date">Date, 10 September, 2030</div>
    <span class="fold" style="top:113px"></span>
    <span class="fold" style="top:164px"></span>
    <span class="fold" style="top:238px"></span>
    <div class="letter__body">
      <p>Lorem ipsum dolor sit amet, consectetur adipisicing elit, sed do eiusmod tempor incididunt ut labore et dolore magna aliqua. Ut enim ad minim veniam, quis nostrud exercitation ullamco laboris nisi ut aliquip ex ea commodo consequat. Duis aute irure dolor in reprehenderit in voluptate velit esse cillum dolore eu fugiat nulla pariatur. Excepteur sint occaecat cupidatat non proident, sunt in culpa qui officia deserunt mollit anim id est laborum. Sed ut perspiciatis unde omnis iste natus error sit voluptatem accusantium doloremque laudantium, totam rem aperiam, eaque ipsa quae ab illo inventore veritatis et quasi architecto beatae vitae dicta sunt explicabo. Nemo enim ipsam voluptatem quia voluptas sit aspernatur aut odit aut fugit, sed quia consequuntur magni dolores eos qui ratione voluptatem sequi nesciunt.</p>
      <p>Lorem ipsum dolor sit amet, consectetur adipisicing elit, sed do eiusmod tempor incididunt ut labore et dolore magna aliqua. Ut enim ad minim veniam, quis nostrud exercitation ullamco laboris nisi ut aliquip ex ea commodo consequat. Duis aute irure dolor in reprehenderit in voluptate velit esse cillum dolore eu fugiat nulla pariatur. Excepteur sint occaecat cupidatat non proident, sunt in culpa qui officia deserunt mollit anim id est laborum. Sed ut perspiciatis unde omnis iste natus error sit voluptatem accusantium doloremque laudantium, totam rem aperiam, eaque ipsa quae ab illo inventore veritatis.</p>
      <p>Lorem ipsum dolor sit amet, consectetur adipisicing elit, sed do eiusmod tempor incididunt ut labore et dolore magna aliqua. Ut enim ad minim veniam, quis nostrud exercitation ullamco laboris nisi ut aliquip ex ea commodo consequat.</p>
    </div>
    <div class="letter__signature" role="img" aria-label="Handschriftliche Unterschrift"></div>
    <div class="letter__signer">NAME SURNAME<span>General Manager</span></div>
  </article>

  <!-- Envelope front -->
  <section class="envelope envelope--front">
    <div class="brand"><div class="brand__name">Tobias Renz</div><div class="brand__role">Rechtsanwalt</div></div>
    <div class="envelope__window"></div>
  </section>

  <!-- Envelope back -->
  <section class="envelope envelope--back">
    <svg class="envelope__flap" width="296" height="47" viewBox="0 0 296 47">
      <path d="M0 0 H296 L284 30 Q278 46 260 46 H36 Q18 46 12 30 Z" fill="#1f3c63"/>
    </svg>
    <div class="brand"><div class="brand__name">Tobias Renz</div><div class="brand__role">Rechtsanwalt</div></div>
  </section>

</main>
</body>
</html>
```